Harborne Cellarbook: the premier wine registry - (need business cards)

We have a logo designed, and now we need business cards for our 3 founders. Harborne Cellarbook is the premier wine registry for weddings. I am envisioning the wine glass with the heart in it as our signature symbol. (FYI- on the red background file, only use the part that has the red background; the brown colors are not relevant)

```html
<!DOCTYPE html>
<html lang="en">
<head>
<meta charset="utf-8">
<title>Harborne Cellarbook – Business Cards</title>
<link href="https://fonts.googleapis.com/css2?family=Lato:wght@400;700&display=swap" rel="stylesheet">
<style>
  :root {
    --wine: #96244e;
    --silver: #c9c9cc;
    --ink-grey: #6d6e71;
    --paper: #ffffff;
    --backdrop: #ecebe8;
  }
  * { margin: 0; padding: 0; box-sizing: border-box; }
  html, body {
    width: 1200px; height: 900px; overflow: hidden;
    background: var(--backdrop);
    font-family: "Lato", sans-serif;
  }
  .sheet {
    position: relative; width: 1200px; height: 900px;
    display: flex; align-items: center; justify-content: center; gap: 50px;
  }
  .card {
    position: relative; width: 525px; height: 300px; overflow: hidden;
    box-shadow: 0 6px 18px rgba(0,0,0,0.18);
  }
  /* Front */
  .card--front { background: var(--wine); color: var(--paper); }
  .brand {
    position: absolute; display: flex; align-items: center; gap: 12px;
    font-weight: 400; letter-spacing: 0.22em; text-transform: uppercase; white-space: nowrap;
  }
  .brand__dot { width: 14px; height: 14px; border-radius: 50%; flex: none; }
  .card--front .brand { left: 0; right: 0; top: 118px; justify-content: center; font-size: 22px; color: var(--paper); }
  .card--front .brand__dot { background: var(--paper); }
  .card--front .website {
    position: absolute; left: 0; right: 0; bottom: 36px; text-align: center;
    font-size: 13px; font-weight: 700; letter-spacing: 0.02em;
  }
  /* Back */
  .card--back { background: var(--paper); }
  .card__wave { position: absolute; inset: 0; width: 100%; height: 100%; }
  .person { position: absolute; left: 32px; top: 40px; }
  .person__name { font-size: 21px; font-weight: 700; color: var(--wine); letter-spacing: 0.02em; }
  .person__role { font-size: 14px; color: var(--ink-grey); margin-top: 1px; }
  .card--back .brand { right: 24px; top: 96px; font-size: 19px; color: var(--wine); }
  .card--back .brand__dot { background: var(--wine); }
  .contact { position: absolute; left: 40px; top: 145px; color: var(--ink-grey); font-size: 15px; line-height: 1.3; font-style: normal; }
  .contact__row { display: flex; align-items: center; gap: 8px; }
  .contact__row svg { width: 14px; height: 14px; fill: var(--wine); flex: none; }
  .contact__address { margin-top: 10px; font-size: 16px; line-height: 1.25; }
  .card--back .website {
    position: absolute; right: 26px; top: 236px; color: var(--paper);
    font-size: 13px; font-weight: 400; white-space: nowrap;
  }
</style>
</head>
<body>
<main class="sheet">
  <section class="card card--front">
    <div class="brand"><span class="brand__dot"></span>Harborne Cellarbook</div>
    <p class="website">www.cellarbook.example</p>
  </section>

  <section class="card card--back">
    <svg class="card__wave" viewBox="0 0 525 300" preserveAspectRatio="none" aria-hidden="true">
      <path d="M0,250 C150,285 330,240 525,118 L525,300 L0,300 Z" fill="var(--silver)"/>
      <path d="M0,262 C155,294 340,250 525,132 L525,300 L0,300 Z" fill="var(--paper)"/>
      <path d="M0,268 C160,298 345,255 525,138 L525,300 L0,300 Z" fill="var(--wine)"/>
    </svg>

    <div class="person">
      <h1 class="person__name">MARCUS ELLERY</h1>
      <p class="person__role">Managing Director</p>
    </div>

    <div class="brand"><span class="brand__dot"></span>Harborne Cellarbook</div>

    <address class="contact">
      <div class="contact__row">
        <svg viewBox="0 0 24 24"><path d="M6.6 10.8a15.1 15.1 0 0 0 6.6 6.6l2.2-2.2a1 1 0 0 1 1-.25 11.4 11.4 0 0 0 3.6.57 1 1 0 0 1 1 1V20a1 1 0 0 1-1 1A17 17 0 0 1 3 4a1 1 0 0 1 1-1h3.5a1 1 0 0 1 1 1c0 1.25.2 2.45.57 3.57a1 1 0 0 1-.25 1z"/></svg>
        <span>044-555 210 348</span>
      </div>
      <div class="contact__row">
        <svg viewBox="0 0 24 24"><path d="M2 5h20v14H2z M2 5l10 8 10-8" fill="var(--wine)" stroke="var(--paper)" stroke-width="1.5"/></svg>
        <span>hello@cellarbook.example</span>
      </div>
      <p class="contact__address">18, Vineyard Row<br>45210, Country Name</p>
    </address>

    <p class="website">www.cellarbook.example</p>
  </section>
</main>
</body>
</html>
```